Halvorn Crest Real estate in need of Logo design

I just started a new real estate brokerage company and need a professional, new logo design that I can incorporate through all forms of marketing and branding. I would like the business card to use both Matte finish and high gloss.

```html
<!DOCTYPE html>
<html lang="en">
<head>
<meta charset="utf-8">
<title>Halvorn Crest Real Estate — Business Cards</title>
<link href="https://fonts.googleapis.com/css2?family=Montserrat:wght@400;600;700;800&family=Nunito+Sans:wght@400;600&display=swap" rel="stylesheet">
<style>
  :root {
    --stage: #2b2b2b;
    --stage-deep: #141414;
    --card: #0e0e0e;
    --card-edge: #1b1b1b;
    --gold: #d4a82a;
    --blue: #19a3e0;
    --white: #f4f4f4;
    --grey: #9c9c9c;
    --rule: #8a8a8a;
  }
  * { box-sizing: border-box; margin: 0; padding: 0; }
  html, body { width: 1200px; height: 1200px; overflow: hidden; }
  body {
    background: radial-gradient(ellipse at 50% 40%, var(--stage) 0%, var(--stage-deep) 85%);
    font-family: "Nunito Sans", Arial, sans-serif;
    position: relative;
  }
  .card {
    position: absolute;
    left: 150px;
    width: 900px;
    height: 514px;
    background: linear-gradient(160deg, var(--card-edge) 0%, var(--card) 60%);
    box-shadow: 0 18px 40px rgba(0,0,0,.6);
  }
  .card--back { top: 60px; }
  .card--front { top: 626px; }

  .brand { display: flex; align-items: center; gap: 22px; }
  .brand__mark { width: 104px; height: 104px; flex: none; }
  .brand__name {
    font-family: "Montserrat", Arial, sans-serif;
    font-weight: 700;
    line-height: 1.15;
    text-transform: uppercase;
  }
  .brand__name span { display: block; }
  .brand__name .brand__sub { letter-spacing: 0.62em; font-size: 0.62em; margin-top: 6px; }

  .card--back .brand { position: absolute; left: 240px; top: 160px; }
  .card--back .brand__mark { background: var(--gold); }
  .card--back .brand__name { color: var(--gold); font-size: 36px; }
  .card--back .site {
    position: absolute; left: 0; right: 0; top: 400px;
    text-align: center; color: var(--white); font-size: 19px; letter-spacing: .03em;
  }

  .card--front .brand { position: absolute; left: 70px; top: 48px; }
  .card--front .brand__mark { background: var(--blue); }
  .card--front .brand__name { color: var(--white); font-size: 38px; }

  .person { position: absolute; left: 70px; top: 232px; }
  .person__name {
    font-family: "Montserrat", Arial, sans-serif; font-weight: 800;
    color: var(--blue); font-size: 30px; letter-spacing: .02em;
  }
  .person__role {
    font-family: "Montserrat", Arial, sans-serif; font-weight: 400;
    color: var(--grey); font-size: 18px; letter-spacing: .06em; margin-top: 2px;
  }
  .divider { position: absolute; left: 70px; right: 70px; top: 312px; height: 1px; background: var(--rule); }

  .contacts { position: absolute; left: 70px; top: 330px; list-style: none; }
  .contacts li { display: flex; align-items: center; gap: 16px; color: var(--white); font-size: 20px; height: 36px; }
  .contacts svg { width: 22px; height: 22px; flex: none; }

  .address {
    position: absolute; right: 70px; bottom: 56px;
    display: flex; align-items: center; gap: 18px;
    border-top: 1px solid var(--rule); padding-top: 12px;
  }
  .address p { color: var(--white); font-size: 22px; line-height: 1.3; text-align: right; }
  .address svg { width: 26px; height: 34px; }
</style>
</head>
<body>

<section class="card card--back">
  <div class="brand">
    <div class="brand__mark"></div>
    <div class="brand__name"><span>Halvorn Crest</span><span class="brand__sub">Real Estate</span></div>
  </div>
  <p class="site">www.halvorncrest.com</p>
</section>

<section class="card card--front">
  <div class="brand">
    <div class="brand__mark"></div>
    <div class="brand__name"><span>Halvorn Crest</span><span class="brand__sub">Real Estate</span></div>
  </div>

  <div class="person">
    <h1 class="person__name">MARCUS DELANEY</h1>
    <p class="person__role">REAL ESTATE BROKER</p>
  </div>
  <div class="divider"></div>

  <ul class="contacts">
    <li>
      <svg viewBox="0 0 24 24"><path fill="#19a3e0" d="M6.6 10.8a15 15 0 0 0 6.6 6.6l2.2-2.2a1 1 0 0 1 1-.25 11.4 11.4 0 0 0 3.6.57 1 1 0 0 1 1 1V20a1 1 0 0 1-1 1A17 17 0 0 1 3 4a1 1 0 0 1 1-1h3.5a1 1 0 0 1 1 1c0 1.25.2 2.45.57 3.6a1 1 0 0 1-.25 1z"/></svg>
      2480-5519-3072
    </li>
    <li>
      <svg viewBox="0 0 24 24"><rect x="2" y="5" width="20" height="14" fill="#19a3e0"/><path d="M2 5l10 8 10-8M2 19l7-7M22 19l-7-7" stroke="#0e0e0e" stroke-width="1.4" fill="none"/></svg>
      info@halvorncrest.com
    </li>
    <li>
      <svg viewBox="0 0 24 24" fill="none" stroke="#19a3e0" stroke-width="1.6"><circle cx="12" cy="12" r="10"/><ellipse cx="12" cy="12" rx="4.5" ry="10"/><path d="M2 12h20M4 7h16M4 17h16"/></svg>
      www.halvorncrest.com
    </li>
  </ul>

  <div class="address">
    <p>2710 Birchmont Road<br>Larkfield, Florida 32190</p>
    <svg viewBox="0 0 24 32"><path fill="#19a3e0" d="M12 0A11 11 0 0 0 1 11c0 8 11 21 11 21s11-13 11-21A11 11 0 0 0 12 0zm0 15.5a4.5 4.5 0 1 1 0-9 4.5 4.5 0 0 1 0 9z"/></svg>
  </div>
</section>

</body>
</html>
```